Corporate Brightfen business cards to be handed to investor, bankers etc. Needs to have a young feel

I need business cards designed for a technology company that provides uber-like rapid response on the security industry. I would like it simple but very cool and tasteful. See attached documents for artwork and colours to be used. Cut sheet describes business model. Card stock should be thicker than normal. I would like the one side to be just the art and the other to have the contact info with maybe the pin somewhere.

Target Market(s)

Investors

Industry/Entity Type

Business

Contact Information for Business Card

Would like the logo attached on one side with name address and other info on the other side.

Font styles to use
Other font styles liked:
• See existing logo

Colors
6b449b
886aae
e4daeb
ffffff

Requirements
Must have
• Name: Dorian Felkatsis
• Address: 47 Larkfield Avenue, Toronto, On, M6K2B7
• Tel: 416-7291846
• Email: rolo@brightfen.io
Nice to have
• See logo colours

```html
<!DOCTYPE html>
<html lang="en">
<head>
<meta charset="utf-8">
<title>Brightfen Business Cards</title>
<link rel="stylesheet" href="https://fonts.googleapis.com/css2?family=Roboto:wght@400;500&display=swap">
<style>
  :root {
    --backdrop: #b9b9b9;
    --brand-purple: #7658a3;
    --brand-purple-mark: #886aae;
    --card-white: #f7f7f7;
    --ink: #1c1c1c;
    --on-purple: #ffffff;
  }
  * { margin: 0; padding: 0; box-sizing: border-box; }
  html, body {
    width: 1200px;
    height: 960px;
    overflow: hidden;
  }
  body {
    position: relative;
    background: var(--backdrop);
    font-family: "Roboto", Arial, sans-serif;
  }
  .card {
    position: absolute;
    left: 320px;
    width: 600px;
    box-shadow: 0 2px 6px rgba(0, 0, 0, 0.25);
  }
  .card--contact {
    top: 100px;
    height: 350px;
    background: var(--brand-purple);
    color: var(--on-purple);
    text-align: center;
  }
  .card--contact .brand-dot {
    position: absolute;
    left: 280px;
    top: 114px;
    width: 40px;
    height: 40px;
    border-radius: 50%;
    background: var(--on-purple);
  }
  .holder-name {
    position: absolute;
    top: 168px;
    left: 0;
    right: 0;
    font-size: 19px;
    font-weight: 500;
  }
  .contact-line {
    position: absolute;
    left: 0;
    right: 0;
    font-size: 14.5px;
    font-weight: 400;
  }
  .contact-line--reach { top: 197px; }
  .contact-line--address { top: 218px; }
  .card--brand {
    top: 493px;
    height: 342px;
    background: var(--card-white);
  }
  .brand-lockup {
    position: absolute;
    left: 0;
    right: 0;
    top: 146px;
    display: flex;
    align-items: center;
    justify-content: center;
    gap: 12px;
  }
  .brand-lockup .brand-dot {
    width: 30px;
    height: 30px;
    border-radius: 50%;
    background: var(--brand-purple-mark);
  }
  .brand-name {
    font-size: 46px;
    font-weight: 400;
    color: var(--ink);
    line-height: 1;
  }
</style>
</head>
<body>
  <section class="card card--contact">
    <span class="brand-dot"></span>
    <h1 class="holder-name">Dorian Felkatsis</h1>
    <p class="contact-line contact-line--reach">416-7291846 | rolo@brightfen.io | www.brightfen.io</p>
    <p class="contact-line contact-line--address">47 Larkfield Avenue, Toronto, On, M6K2B7</p>
  </section>

  <section class="card card--brand">
    <div class="brand-lockup">
      <span class="brand-dot"></span>
      <span class="brand-name">Brightfen</span>
    </div>
  </section>
</body>
</html>
```